Small business offering independent forensic science consultancy requires flyer and magnet design

We had great success in obtaining a logo design using pixel harbor and we are hoping to draw on your expertise again!

Clearwater Evidence Advisors is a small consultancy business that mainly involves reviewing forensic case files for both the prosecution and defence, and providing expert opinion on the findings in the form of a report, as well as attending court as an expert witness.

Our areas of expertise currently is Forensic Biology (analysis of body fluids), DNA analysis and bloodstain pattern analysis, but this may grow in the future. You can find further information as well as obtain a bit of a feel for the style we are looking for from our website www.clearwaterevidenceadvisors.com.au.

The flyer should be clean and professional looking and we have attached files including our logo and and a Plumtree Text Doc containing the wording for inclusion in the flyer. We have attached an 'ímage feel' document to give you a feel for the types of images we like - but we own all the images on our website, so please contact me if you want to use any of these images and I can send you the files - however are open to any other images in keeping with our website and brand feel.

We will consider various format options such as tri-fold, bi-fold, however,DL sized bi-fold is probably a slight preference. We are also open to suggestions from designers. We would also like to have the capability to modify our wording on the flyer as we have not completely locked it in as yet.

Please note that the brief is also to include the design of a simple advertising magnet to supplement our flyers. They will also be given out separately. The magnet should be a simple design for standard size (90mm x 45mm) magnet, similar to a business card with logo, tagline and contact details (information contained in attached file).

We look forward to seeing your design ideas. Thanks!
Updates

We will be extending the deadline for this project to the 10th January, to allow designers plenty of time given the time of year! 

Thanks to all the designers who have submitted designs so far - as it is the Christmas and New Year period, I will be extending the deadline by one week to allow time for all of you who have accepted my invitation to submit a design.

We will provide individual feedback over the next week to those who have submitted designs. 

We've had some great designs so far - and look forward to seeing some more!

Many thanks!

Hi designers - thanks for the designs submitted so far.  We have provided feedback to all designs under consideration - and welcome re-submissions with the alterations we have suggested.

The deadline will stay at the 10th Jan, so please finalise your designs and re-submit before this date.

We are also still open to considering new designs at this stage.

Kind regards

Marta

Target Market(s)

The criminal law and law enforcement communities including solicitors, barristers, and detectives.

Industry/Entity Type

Advertising

Requirements
Must have
• Clearwater Evidence Advisors Logo
Clearwater Evidence Advisors Tagline
At least one of the images from our website
Nice to have
• Other images that fit with the picture scheme on our website and in the reference pictures attached.
Should not have
• pictures of fingerprints, deceased, glamorised crime scenes, police or vbq references.

```html
<!DOCTYPE html>
<html lang="en">
<head>
<meta charset="utf-8">
<title>Clearwater Evidence Advisors – Brochure</title>
<link rel="stylesheet" href="https://fonts.googleapis.com/css2?family=Source+Sans+3:wght@400;600&display=swap">
<style>
  :root {
    --bg: #e4e4e4;
    --paper: #ffffff;
    --brand-blue: #2f9fcf;
    --panel-blue: #34a9da;
    --logo-blue: #1f5fa8;
    --ink: #2b3a48;
    --ink-soft: #4a5a68;
    --lab-light: #dfe7ee;
    --lab-mid: #a9bccb;
    --vial-purple: #5b2f9b;
    --vial-amber: #c98a4e;
    --molecule: #bfe0f2;
  }
  * { box-sizing: border-box; margin: 0; padding: 0; }
  html, body { width: 1200px; height: 800px; overflow: hidden; }
  body {
    background: var(--bg);
    font-family: "Source Sans 3", Arial, sans-serif;
    color: var(--ink);
    position: relative;
  }
  .panel {
    position: absolute;
    top: 95px;
    width: 420px;
    height: 610px;
    background: var(--paper);
    box-shadow: 0 2px 8px rgba(0,0,0,0.12);
    overflow: hidden;
  }
  .cover { left: 165px; }
  .back { left: 615px; }

  /* brand name */
  .brand {
    display: flex;
    align-items: center;
    gap: 8px;
    color: var(--logo-blue);
    font-weight: 400;
    font-size: 22px;
    line-height: 1.05;
  }
  .brand-dot {
    width: 30px; height: 30px;
    border-radius: 50%;
    background: var(--logo-blue);
    flex: none;
  }

  /* cover */
  .cover .brand { position: absolute; left: 75px; top: 92px; width: 300px; }
  .photo-grid {
    position: absolute;
    left: 75px; top: 185px;
    width: 295px; height: 285px;
    display: grid;
    grid-template-columns: 97px 97px 95px;
    grid-template-rows: 95px 95px 89px;
    gap: 3px;
    background: #1c1c1c;
  }
  .photo { background: linear-gradient(135deg, var(--lab-light), var(--lab-mid)); }
  .photo.a { grid-column: 1 / 3; grid-row: 1; background: linear-gradient(135deg, #cfe3ee, #8fb2c8); }
  .photo.b { grid-column: 3; grid-row: 1 / 3; background: linear-gradient(160deg, #e8ecef, #9fb3c2); }
  .photo.c { grid-column: 1; grid-row: 2 / 4; background: linear-gradient(150deg, #eef1f3, #b6c5cf); }
  .photo.d { grid-column: 2; grid-row: 2; background: linear-gradient(135deg, #b9c8c4, #6f8a86); }
  .photo.e { grid-column: 2 / 4; grid-row: 3; background: linear-gradient(135deg, #e6e2dc, #b7c3ca); }
  .cover-band {
    position: absolute;
    left: 0; right: 0; bottom: 0;
    height: 135px;
    background: var(--brand-blue);
    color: #fff;
    display: flex;
    align-items: center;
    justify-content: center;
    text-align: center;
  }
  .tagline { font-weight: 600; font-size: 19px; line-height: 1.35; }

  /* back panel */
  .who {
    height: 238px;
    background: var(--panel-blue);
    padding: 42px 40px 0 46px;
  }
  .who h2 { font-size: 13px; font-weight: 600; color: var(--ink); }
  .who p { font-size: 10.5px; line-height: 1.35; color: var(--ink); margin-top: 3px; }
  .who ul { margin-top: 14px; padding-left: 30px; font-size: 10px; color: var(--ink); }
  .who li { margin-bottom: 11px; }
  .vials {
    height: 80px;
    background: linear-gradient(180deg, var(--vial-purple), #7a3fb0 50%, var(--vial-amber) 110%);
  }
  .back-logo {
    height: 175px;
    display: flex;
    flex-direction: column;
    align-items: center;
    justify-content: flex-end;
    padding-bottom: 6px;
  }
  .back-logo .brand { font-size: 18px; width: 230px; }
  .back-logo .brand-dot { width: 24px; height: 24px; }
  .contact {
    position: absolute;
    left: 0; right: 0; top: 493px;
    text-align: center;
    font-size: 8.5px;
    line-height: 1.5;
    color: var(--ink);
    z-index: 1;
  }
  .contact h3 { font-size: 9px; font-weight: 600; }
  .molecules {
    height: 117px;
    background: linear-gradient(180deg, #e3f2fa, var(--molecule));
  }
</style>
</head>
<body>
  <section class="panel cover">
    <div class="brand"><span class="brand-dot"></span><span>Clearwater<br>Evidence Advisors</span></div>
    <div class="photo-grid">
      <div class="photo a" role="img" aria-label="Scientist in protective mask and glasses holding a flask beside a microscope"></div>
      <div class="photo b" role="img" aria-label="Two scientists examining a sample together"></div>
      <div class="photo c" role="img" aria-label="Scientist working at a microscope"></div>
      <div class="photo d" role="img" aria-label="Laboratory samples on a bench"></div>
      <div class="photo e" role="img" aria-label="Scientist using a pipette in the lab"></div>
    </div>
    <div class="cover-band">
      <p class="tagline">Forensic Science Expertise<br>From The Crime Scene To Court</p>
    </div>
  </section>

  <section class="panel back">
    <div class="who">
      <h2>Who Uses Us?</h2>
      <p>Our services are utilised across the legal and law enforcement communities, some of the organisations that we have completed work for include:</p>
      <ul>
        <li>Private law firms</li>
        <li>Legal Aid</li>
        <li>Aboriginal Legal Aid</li>
        <li>Universities</li>
      </ul>
    </div>
    <div class="vials" role="img" aria-label="Row of glass test tubes lit in purple"></div>
    <div class="back-logo">
      <div class="brand"><span class="brand-dot"></span><span>Clearwater<br>Evidence Advisors</span></div>
    </div>
    <div class="contact">
      <h3>Contact Us</h3>
      <p>Phone: +61 455 210 387</p>
      <p>Email: enquiries@clearwaterevidenceadvisors.com.au</p>
      <p>Web: www.clearwaterevidenceadvisors.com.au</p>
      <p>Mail: PO Box 318 Westbrook NSW Australia 2199</p>
    </div>
    <div class="molecules" role="img" aria-label="Soft blue molecular structure background"></div>
  </section>
</body>
</html>
```